pathology learning flashcard template graphic design .

Creative designs for 2 sides of the flashcards to include colorful sectioning and font sizes that will make it easy to use in studying.

```html
<!DOCTYPE html>
<html lang="en">
<head>
<meta charset="utf-8">
<title>Pathology Flashcard – Gastrointestinal 0001</title>
<link href="https://fonts.googleapis.com/css2?family=Barlow:wght@500;600;700&family=Arimo:wght@400;700&display=swap" rel="stylesheet">
<style>
  :root{
    --red:#d42037;
    --grey:#c9c9cb;
    --ink:#2b2b2d;
    --paper:#ffffff;
    --bg:#e4e4e4;
    --art-light:#f4e2d6;
    --art-mid:#e6b8a4;
  }
  *{margin:0;padding:0;box-sizing:border-box}
  html,body{width:1200px;height:835px;overflow:hidden;background:var(--bg)}
  body{position:relative;font-family:"Arimo",Arial,sans-serif;color:var(--ink)}

  .card{position:absolute;width:620px;height:390px;background:var(--paper);overflow:hidden;box-shadow:0 2px 8px rgba(0,0,0,.12)}
  .card--front{left:40px;top:22px}
  .card--back{left:540px;top:423px}

  /* front */
  .front-header{position:absolute;left:0;top:0;width:620px;height:82px}
  .category{position:absolute;left:22px;top:28px;font-family:"Barlow",sans-serif;font-weight:700;font-size:29px;letter-spacing:.5px;line-height:1;color:#fff;white-space:nowrap}
  .case-id{position:absolute;left:374px;top:36px;font-family:"Barlow",sans-serif;font-weight:700;font-size:14px;letter-spacing:.5px;line-height:1;color:var(--ink);white-space:nowrap}
  .case-id__num{color:var(--red);font-size:22px;margin-left:6px;vertical-align:-3px}
  .anatomy-art{position:absolute;left:22px;top:98px;width:180px;height:262px;border-radius:50% 50% 20% 20%/30% 30% 10% 10%;background:radial-gradient(ellipse at 50% 60%,var(--art-mid),var(--art-light) 60%,#fff 90%)}
  .case{position:absolute;left:214px;top:100px;width:388px}
  .case__stem{font-size:12.4px;line-height:16.5px;text-align:justify}
  .case__question{margin-top:12px;font-weight:700;font-size:12.4px}
  .options{display:grid;grid-template-columns:1fr 1fr;gap:2px 10px;margin-top:6px;font-size:12.4px;list-style:none}
  .front-footer{position:absolute;left:0;bottom:0;width:100%;height:16px;background:var(--red)}

  /* back */
  .back-topband{position:absolute;left:0;top:0;width:100%;height:18px;background:var(--grey)}
  .back-titlezone{position:absolute;left:0;top:0;width:218px;height:82px;background:var(--grey)}
  .diagnosis-title{position:absolute;left:22px;top:26px;font-family:"Barlow",sans-serif;font-weight:700;font-size:34px;line-height:1.1;color:var(--ink)}
  .definition{position:absolute;left:234px;top:26px;width:370px;font-size:11.5px;line-height:14.5px}
  .definition__label{color:var(--red);font-weight:700}
  .answer-panel{position:absolute;left:0;top:82px;width:218px;height:308px;background:var(--red);color:#fff;padding:12px 16px 0 18px}
  .answer-panel__head{font-size:14px;margin-bottom:8px}
  .answer-panel__head b{font-weight:700}
  .answer-panel p{font-size:10.4px;line-height:13.2px}
  .notes{position:absolute;left:234px;top:70px;width:372px}
  .note{margin-bottom:8px;font-size:10.4px;line-height:13px}
  .note__label{display:block;color:var(--red);font-weight:700;font-size:12px;margin-bottom:1px}
  .note__label--inline{display:inline;margin-right:3px}
  .sources{position:absolute;left:234px;bottom:8px;font-size:7.5px;font-style:italic;color:#555}
  .page-num{position:absolute;right:-18px;bottom:-18px;width:62px;height:62px;border-radius:50%;background:var(--grey);font-size:11px;padding:14px 0 0 18px}
</style>
</head>
<body>

<article class="card card--front">
  <svg class="front-header" viewBox="0 0 620 82" aria-hidden="true">
    <rect x="0" y="0" width="620" height="82" fill="#c9c9cb"/>
    <path d="M0 0H620V20H372C360 20 356 28 352 40C348 56 342 70 328 70H0Z" fill="#d42037"/>
    <rect x="0" y="78" width="620" height="4" fill="#fff"/>
  </svg>
  <h1 class="category">GASTROINTESTINAL</h1>
  <div class="case-id">PATHOLOGY CASE ID:<span class="case-id__num">0001</span></div>

  <div class="anatomy-art" role="img" aria-label="Labelled illustration of the human digestive tract: mouth, esophagus, stomach, small and large intestine, rectum and anus"></div>

  <section class="case">
    <p class="case__stem">50-year-old woman comes to the clinic because she has difficulty swallowing for the past few months. She says symptoms have been worsening. She also complains of cough, mostly at night and in fear of choking, has stopped eating many foods, losing about 12 lbs in the past 3 months. Past medical history is unremarkable. Vital signs are normal and physical exam is unremarkable. Chest x-ray with demonstrates an air-fluid level, while manometry shows absent relaxation of the lower esophageal sphincter during swallowing.</p>
    <p class="case__question">What is the most likely diagnosis?</p>
    <ul class="options">
      <li>A) GERD</li>
      <li>C) Achalasia</li>
      <li>B) Barret Esophagus</li>
      <li>D) Eosinophilic Esophagitis</li>
    </ul>
  </section>
  <div class="front-footer"></div>
</article>

<article class="card card--back">
  <div class="back-topband"></div>
  <div class="back-titlezone"></div>
  <h2 class="diagnosis-title">Achalasia</h2>
  <p class="definition"><span class="definition__label">[Definition]</span> Motility disorder where esophageal relaxation is impaired in the lower esophageal sphincter (LES).</p>

  <aside class="answer-panel">
    <p class="answer-panel__head"><b>ANS:</b> (C) Achalasia</p>
    <p>Symptoms and studies suggestive of achalasia. Patient's manometry presents with no relaxation of the lower esophageal sphincter during swallowing. Patient also complains of dysphagia and is unable to swallow properly, leading to weight loss. Patient has no past infection or inflammation, ruling out eosinophilic esophagitis. Patient does not have chronic GERD, eliminating the possibility of Barrett esophagus, in which at least 5 years of acid reflux are beforehand to develop columnar metaplasia.</p>
  </aside>

  <section class="notes">
    <p class="note"><span class="note__label">Etiology/ Pathology:</span>Destruction of inhibitory neurons in the Auerbach plexus. Loss of peristalsis in the lower esophageal sphincter (Lower-two thirds of the esophagus)</p>
    <p class="note"><span class="note__label">P/E and Symptoms:</span>Dysphagia that is progressive, regurgitation, weight-loss, dry cough, chest pain, GERD, esophageal perforation, squamous cell carcinoma, aspiration pneumonia.</p>
    <p class="note"><span class="note__label note__label--inline">Dx:</span>Barium swallow will show 'bird's beak' and esophageal dilation. Manometry will present with increased resting lower esophageal sphincter pressure. Endoscopy will usually present with normal mucosa and LES dilation, and in some cases residual material such as undigested food particles may be present.</p>
    <p class="note"><span class="note__label note__label--inline">Rx:</span>First line of treatment are nitrates, calcium channel blockers, and Botulinum toxin injection in the LES. Long term management options include esophageal dilation with pneumatic balloon and myotomy.</p>
  </section>
  <p class="sources">Harlow's Drug Guide; Veridan Pocket Formulary; medreflib.com; clinnotes.org</p>
  <div class="page-num">1</div>
</article>

</body>
</html>
```